Medical Cannabis company is looking for a LOGO design *

SILVER PETALWORKS (SP) is a new company in the Israeli medical cannabis industry. We will engage in PREMIUM medical cannabis growing and cultivation and also manufacturing of HIGH-END cannabis based medical products.
the design should reflect luxury, high-end and Pharma-grade products.
the design should use color GOLD and NOT using the famous cannabis leaf !

Target Market(s)

international medical cannabis Pharmaceutical companies
and of course local and international patients

Contact Information for Business Card

Yoav Ben-Ami
Founder and CEO

Silver Petalworks
Medical grade cannabis

yoavbenami@mailnest.example
972-52-3186907

Colors
ffc214
fbed22

Requirements
Must have
• clean and simple
• luxury
• gold !!
• (can also have green for Cannabis and/or blue for Pharma)
Should not have
• cannabis leaf

```html
<!DOCTYPE html>
<html lang="en">
<head>
<meta charset="utf-8">
<title>Silver Petalworks – Business Card</title>
<link rel="stylesheet" href="https://fonts.googleapis.com/css2?family=Jost:wght@400;500&display=swap">
<style>
  :root {
    --page: #ffffff;
    --card-dark: #1f1f1f;
    --gold-text: #e9c07f;
    --gold-rule: #e4b26e;
    --glitter-light: #c7b35a;
    --glitter-mid: #9c8a36;
    --glitter-deep: #6f6222;
  }
  * { margin: 0; padding: 0; box-sizing: border-box; }
  html, body {
    width: 1200px; height: 1000px; overflow: hidden;
    background: var(--page);
    font-family: "Jost", "Futura", sans-serif;
  }
  .canvas { position: relative; width: 1200px; height: 1000px; }
  .card { position: absolute; left: 308px; width: 613px; height: 350px; }
  .card--front { top: 91px; }
  .card--back { top: 521px; }
  .card-art { position: absolute; inset: 0; width: 613px; height: 350px; display: block; }
  .glitter-stop-a { stop-color: var(--glitter-light); }
  .glitter-stop-b { stop-color: var(--glitter-mid); }
  .glitter-stop-c { stop-color: var(--glitter-deep); }
  .fill-dark { fill: var(--card-dark); }
  .fill-rule { fill: var(--gold-rule); }

  .brand {
    position: absolute; left: 0; right: 0; top: 158px;
    text-align: center; color: var(--gold-text);
  }
  .brand-name { font-size: 28px; font-weight: 500; letter-spacing: 0.5px; line-height: 1; }
  .brand-tagline { margin-top: 12px; font-size: 17px; font-weight: 400; line-height: 1; }
  .brand-tagline .star { font-size: 17px; margin: 0 10px; }

  .person-name {
    position: absolute; left: 0; right: 0; top: 96px;
    text-align: center; color: var(--gold-text);
    font-size: 38px; font-weight: 500; line-height: 1; letter-spacing: 0.5px;
  }
  .person-name .star { font-size: 30px; vertical-align: 4px; }
  .contact-list {
    position: absolute; left: 151px; top: 166px;
    list-style: none; color: var(--gold-text); font-size: 19px; line-height: 1;
  }
  .contact-item { display: flex; height: 37px; }
  .contact-label { width: 73px; }
  .contact-sep { width: 18px; }
</style>
</head>
<body>
<main class="canvas">

  <section class="card card--front" aria-label="Business card front">
    <svg class="card-art" viewBox="0 0 613 350" aria-hidden="false">
      <defs>
        <linearGradient id="glitter" x1="0" y1="0" x2="1" y2="1">
          <stop offset="0" class="glitter-stop-b"/>
          <stop offset="0.5" class="glitter-stop-a"/>
          <stop offset="1" class="glitter-stop-c"/>
        </linearGradient>
      </defs>
      <rect width="613" height="350" fill="url(#glitter)" role="img" aria-label="Gold glitter texture"/>
      <rect class="fill-dark" x="0" y="77" width="613" height="219"/>
      <rect class="fill-rule" x="0" y="296" width="613" height="5"/>
      <polygon class="fill-rule" points="0,70 613,8 613,12 0,74"/>
      <polygon class="fill-dark" points="0,74 613,12 613,20 0,82"/>
    </svg>
    <div class="brand">
      <h1 class="brand-name">SILVER PETALWORKS</h1>
      <p class="brand-tagline"><span class="star">★</span>Medical grade cannabis<span class="star">★</span></p>
    </div>
  </section>

  <section class="card card--back" aria-label="Business card back">
    <svg class="card-art" viewBox="0 0 613 350">
      <defs>
        <linearGradient id="glitter-back" x1="0" y1="0" x2="1" y2="1">
          <stop offset="0" class="glitter-stop-b"/>
          <stop offset="0.5" class="glitter-stop-a"/>
          <stop offset="1" class="glitter-stop-c"/>
        </linearGradient>
      </defs>
      <rect width="613" height="350" fill="url(#glitter-back)" role="img" aria-label="Gold glitter texture"/>
      <rect class="fill-rule" x="0" y="48" width="613" height="5"/>
      <rect class="fill-dark" x="0" y="53" width="613" height="230"/>
      <polygon class="fill-dark" points="0,338 613,283 613,291 0,345"/>
      <polygon class="fill-rule" points="0,345 613,291 613,295 0,350"/>
    </svg>
    <h2 class="person-name"><span class="star">★</span>YOAV BEN-AMI<span class="star">★</span></h2>
    <ul class="contact-list">
      <li class="contact-item"><span class="contact-label">Email</span><span class="contact-sep">:</span><span class="contact-value">Yoavbenami@mailnest.example</span></li>
      <li class="contact-item"><span class="contact-label">Phone</span><span class="contact-sep">:</span><span class="contact-value">( 972 )-52-3186907</span></li>
    </ul>
  </section>

</main>
</body>
</html>
```